Food truck menu design

Looking for a menu to be dissed for my toasted sandwich food truck. I have attached to logo and photo of the food truck for inspiration. if it can tie into them.
needing three sections, with titles:
CLASSICS
- classic one
. description
-Classic two
. Description
PREMIUM
- Premium one
. description
-Premium Two
. Description
-Premium Three
. Description
DESERT
-Desert one
. Description
-Desert two
.Description

also if it can be editable so I can change menu items and descriptions.

```html
<!DOCTYPE html>
<html lang="en">
<head>
<meta charset="utf-8">
<title>Marlo's Melts – Food Truck Menu</title>
<link rel="stylesheet" href="https://fonts.googleapis.com/css2?family=Cinzel:wght@700&family=Lora:ital@1&family=Permanent+Marker&family=Syncopate:wght@700&display=swap">
<style>
  :root {
    --menu-orange: #e06a00;
    --heading-red: #a8140f;
    --ink: #111111;
    --title-white: #ffffff;
    --badge-cream: #fdf3d6;
    --badge-ink: #3a1a12;
  }
  html, body {
    margin: 0;
    padding: 0;
    overflow: hidden;
  }
  .menu {
    position: relative;
    width: 1200px;
    height: 927px;
    background: var(--menu-orange);
    overflow: hidden;
    font-family: "Lora", serif;
    color: var(--ink);
  }
  .brand {
    position: absolute;
    left: 40px;
    top: 24px;
    width: 270px;
    height: 270px;
    border-radius: 50%;
    background: var(--badge-cream);
    display: flex;
    align-items: center;
    justify-content: center;
  }
  .brand-name {
    font-family: "Permanent Marker", cursive;
    font-size: 40px;
    color: var(--badge-ink);
    text-align: center;
    line-height: 1.05;
  }
  .menu-title {
    position: absolute;
    left: 300px;
    top: 140px;
    width: 760px;
    margin: 0;
    transform: rotate(-20deg);
    transform-origin: center;
    font-family: "Syncopate", sans-serif;
    font-weight: 700;
    font-style: italic;
    font-size: 78px;
    line-height: 0.95;
    color: var(--title-white);
    text-align: center;
    letter-spacing: 1px;
  }
  .menu-title .line-two {
    display: block;
    margin-left: -90px;
  }
  .section-heading {
    position: absolute;
    margin: 0;
    font-family: "Cinzel", serif;
    font-weight: 700;
    font-size: 42px;
    color: var(--heading-red);
    letter-spacing: 1px;
    text-align: center;
    width: 360px;
  }
  .heading-classics { left: 20px; top: 338px; }
  .heading-desert { left: 423px; top: 335px; }
  .heading-premium { left: 835px; top: 163px; }
  .menu-item {
    position: absolute;
    width: 350px;
  }
  .item-row {
    display: flex;
    align-items: baseline;
    white-space: nowrap;
  }
  .item-name {
    font-family: "Permanent Marker", cursive;
    font-size: 24px;
  }
  .item-leader {
    font-family: "Lora", serif;
    font-style: normal;
    font-size: 20px;
    letter-spacing: 1px;
  }
  .item-price {
    font-family: "Cinzel", serif;
    font-weight: 700;
    font-size: 28px;
    margin-left: 4px;
  }
  .item-desc {
    margin: 24px 0 0;
    font-style: italic;
    font-size: 16.5px;
    line-height: 22px;
    text-align: center;
    padding-left: 4px;
  }
  .classic-one { left: 29px; top: 430px; }
  .classic-two { left: 29px; top: 655px; }
  .desert-one { left: 436px; top: 432px; }
  .desert-two { left: 436px; top: 637px; }
  .premium-one { left: 829px; top: 249px; }
  .premium-two { left: 835px; top: 439px; }
  .premium-three { left: 835px; top: 651px; }
</style>
</head>
<body>
<main class="menu">
  <div class="brand" role="img" aria-label="Marlo's Melts brand badge">
    <span class="brand-name">Marlo's<br>Melts</span>
  </div>

  <h1 class="menu-title">FOOD TRUCK<span class="line-two">FOOD MENU</span></h1>

  <h2 class="section-heading heading-classics">CLASSICS</h2>
  <h2 class="section-heading heading-desert">DESERT</h2>
  <h2 class="section-heading heading-premium">PREMIUM</h2>

  <section class="menu-item classic-one">
    <div class="item-row"><span class="item-name">Classic one</span><span class="item-leader">...........</span><span class="item-price">$0.0</span></div>
    <p class="item-desc">description,description,description,-<br>descriptidescription,de-<br>scription,on,description,</p>
  </section>
  <section class="menu-item classic-two">
    <div class="item-row"><span class="item-name">Classic one</span><span class="item-leader">...........</span><span class="item-price">$0.0</span></div>
    <p class="item-desc">description,description,description,-<br>descriptidescription,de-<br>scription,on,description,</p>
  </section>

  <section class="menu-item desert-one">
    <div class="item-row"><span class="item-name">Desert one</span><span class="item-leader">............&nbsp;</span><span class="item-price">$0.0</span></div>
    <p class="item-desc">description,description,description,-<br>descriptidescription,de-<br>scription,on,description,</p>
  </section>
  <section class="menu-item desert-two">
    <div class="item-row"><span class="item-name">Desert two</span><span class="item-leader">............&nbsp;</span><span class="item-price">$0.0</span></div>
    <p class="item-desc">description,description,description,-<br>descriptidescription,de-<br>scription,on,description,</p>
  </section>

  <section class="menu-item premium-one">
    <div class="item-row"><span class="item-name">Premium one</span><span class="item-leader">........</span><span class="item-price">$0.0</span></div>
    <p class="item-desc">description,description,description,-<br>descriptidescription,de-<br>scription,on,description,</p>
  </section>
  <section class="menu-item premium-two">
    <div class="item-row"><span class="item-name">Premium two</span><span class="item-leader">........&nbsp;</span><span class="item-price">$0.0</span></div>
    <p class="item-desc">description,description,description,-<br>descriptidescription,de-<br>scription,on,description,</p>
  </section>
  <section class="menu-item premium-three">
    <div class="item-row"><span class="item-name">Premium three</span><span class="item-leader">.....</span><span class="item-price">$0.0</span></div>
    <p class="item-desc">description,description,description,-<br>descriptidescription,de-<br>scription,on,description,</p>
  </section>
</main>
</body>
</html>
```